Poster - to Promote Study Skills

I have written a book about study skills for students. I want to move to using the book to give presentations. This poster looks to emphasise the fact that time is not the most important element of creating study impact, it is the intensity of the effort. The steps outline the increasing effectiveness of a study effort. The highest steps are the most effective. I have done a very rough design. It was written in the excel document, and there is a screen shot of it in the word document. I have done it is landscape, however I think it might be more effective in a portrait format.

Target Market(s)

Students aged 13 to 21

Requirements
Must have
• The 'steps' included in the files
Nice to have
• Would like to have design features, maybe colours, that support the fact that the higher 'study steps' are better.

```html
<!DOCTYPE html>
<html lang="en">
<head>
<meta charset="utf-8">
<title>Your Study Impact – Study Skills Poster</title>
<link rel="stylesheet" href="https://fonts.googleapis.com/css2?family=Bebas+Neue&family=Lato:ital,wght@0,400;0,700;0,900;1,700;1,900&display=swap">
<style>
  :root{
    --orange:#f7941d;
    --plum:#5a1a44;
    --step1:#5c1745;
    --step2:#7e2c64;
    --step3:#a91d47;
    --step4:#d52b35;
    --step5:#f0622f;
    --step6:#f7941d;
    --tread:#8e1230;
    --grey-title:#8a8a8a;
    --ink:#2b2b2b;
    --backdrop:#ececec;
  }
  *{box-sizing:border-box;margin:0;padding:0}
  html,body{width:1200px;height:1200px;overflow:hidden;background:var(--backdrop)}
  .poster{position:absolute;left:135px;top:0;width:930px;height:1200px;background:#fff;overflow:hidden;font-family:"Lato",Arial,sans-serif;color:var(--ink)}

  .headline{position:absolute;left:0;width:100%;display:flex;align-items:center;justify-content:center;font-family:"Bebas Neue","Oswald",sans-serif;color:#fff;letter-spacing:1px;line-height:1;font-weight:400}
  .headline--top{top:0;height:90px;background:var(--orange);font-size:72px;padding-top:6px}
  .headline--formula{top:90px;height:94px;background:var(--plum);font-size:76px;padding-top:6px}

  .clock-icon{position:absolute;left:34px;top:226px;width:140px;height:140px}
  .formula-title{position:absolute;left:32px;top:366px;font-weight:900;font-style:italic;font-size:35px;line-height:44px;color:var(--grey-title)}
  .formula-rule{position:absolute;left:0;top:501px;width:266px;height:3px;background:var(--orange)}
  .formula-rule::after{content:"";position:absolute;right:-6px;top:-5px;width:13px;height:13px;border-radius:50%;background:var(--orange)}

  .stair-sweep{position:absolute;left:12px;top:950px;width:56px;height:56px}

  .step,.step-shadow{position:absolute;width:132px;border-radius:0 0 66px 66px}
  .step-shadow{background:var(--tread);transform:translate(-14px,12px)}
  .step{color:#fff;text-align:center;padding:10px 5px 0;display:flex;flex-direction:column;align-items:center}
  .step__icon{width:36px;height:36px;margin-bottom:4px}
  .step__title{font-weight:900;font-size:13.5px;line-height:14px;text-transform:uppercase}
  .step__rate{margin:6px 0;background:#fff;border-radius:14px;width:100px;padding:3px 0;font-weight:700;font-size:11.5px;line-height:12px}
  .step__text{font-size:10px;line-height:12.2px}

  .step--foundation{left:55px;top:765px;height:242px;background:var(--step1)}
  .step--foundation .step__rate{color:var(--step1)}
  .step--single{left:191px;top:663px;height:259px;background:var(--step2)}
  .step--single .step__rate{color:var(--step2)}
  .step--mindset{left:333px;top:557px;height:306px;background:var(--step3)}
  .step--mindset .step__rate{color:var(--step3)}
  .step--smarter{left:474px;top:450px;height:290px;background:var(--step4)}
  .step--smarter .step__rate{color:var(--step4)}
  .step--balance{left:614px;top:344px;height:236px;background:var(--step5)}
  .step--balance .step__rate{color:var(--step5)}
  .step--aspire{left:754px;top:268px;height:222px;background:var(--step6);padding-top:0}
  .step--aspire .step__rate{color:var(--step6)}
  .step--aspire .step__icon{margin-top:-26px;position:relative}
  .arrow-head{position:absolute;left:730px;top:232px;width:180px;height:38px}

  .portrait{position:absolute;left:786px;width:120px;height:120px;border-radius:50%;border:4px solid;background:#fff;padding:5px}
  .portrait span{display:block;width:100%;height:100%;border-radius:50%;background:radial-gradient(circle at 50% 40%,#9a9a9a,#3e3e3e)}
  .portrait--one{top:628px;border-color:var(--orange)}
  .portrait--two{top:818px;border-color:var(--step4)}
  .portrait--three{top:998px;border-color:var(--step2)}

  .quote{position:absolute;right:20px;text-align:right;font-style:italic;font-size:13px;line-height:16px;color:var(--ink)}
  .quote cite{font-style:normal;display:block;font-size:13px}
  .quote .name{font-weight:700}
  .quote .role{color:#8a8a8a}
  .quote small{display:block;font-style:normal;font-size:7.5px;line-height:9px;color:#999}
  .quote--one{top:762px}
  .quote--one .name{color:var(--orange)}
  .quote--two{top:948px}
  .quote--two .name{color:var(--step4)}
  .quote--three{top:1128px}
  .quote--three .name{color:var(--step2)}

  .footer-band{position:absolute;left:0;bottom:0;width:100%;height:14px;background:var(--step2)}
</style>
</head>
<body>
<main class="poster">
  <h1 class="headline headline--top">Your Study Impact</h1>
  <h2 class="headline headline--formula">= Intensity of Effort x Time</h2>

  <svg class="clock-icon" viewBox="0 0 140 140" aria-hidden="true">
    <defs>
      <linearGradient id="clockGrad" x1="0" y1="0" x2="1" y2="1">
        <stop offset="0" stop-color="#f7941d"/>
        <stop offset="1" stop-color="#5a1a44"/>
      </linearGradient>
    </defs>
    <path d="M22 58 A52 52 0 1 1 28 100" fill="none" stroke="url(#clockGrad)" stroke-width="13" stroke-linecap="round"/>
    <polygon points="4,52 40,50 22,78" fill="#f7941d"/>
    <path d="M72 38 V74 L96 92" fill="none" stroke="#5a1a44" stroke-width="8" stroke-linecap="round" stroke-linejoin="round"/>
  </svg>

  <p class="formula-title">The Formula for<br>Banking High Performance<br>Study Impacts</p>
  <div class="formula-rule"></div>

  <svg class="stair-sweep" viewBox="0 0 56 56" aria-hidden="true">
    <polygon points="0,56 56,56 56,0 40,0" fill="#a3162b"/>
  </svg>

  <div class="step-shadow" style="left:55px;top:765px;height:242px"></div>
  <div class="step-shadow" style="left:191px;top:663px;height:259px"></div>
  <div class="step-shadow" style="left:333px;top:557px;height:306px"></div>
  <div class="step-shadow" style="left:474px;top:450px;height:290px"></div>
  <div class="step-shadow" style="left:614px;top:344px;height:236px"></div>
  <div class="step-shadow" style="left:754px;top:268px;height:222px"></div>

  <section class="step step--foundation">
    <svg class="step__icon" viewBox="0 0 36 36" fill="none" stroke="#fff" stroke-width="2" stroke-linejoin="round" aria-hidden="true">
      <path d="M4 6 V20 L12 30 H16 V20 L10 12"/><path d="M32 6 V20 L24 30 H20 V20 L26 12"/>
    </svg>
    <h3 class="step__title">Building<br>a Foundation</h3>
    <p class="step__rate">$10 an Hour<br>Study Effort</p>
    <p class="step__text">Study time is supported by engagement in class</p>
  </section>

  <section class="step step--single">
    <svg class="step__icon" viewBox="0 0 36 36" fill="none" stroke="#fff" stroke-width="2" stroke-linejoin="round" aria-hidden="true">
      <rect x="7" y="5" width="22" height="28" rx="2"/><rect x="13" y="2" width="10" height="6" rx="1"/><path d="M12 20 L16 24 L24 15"/>
    </svg>
    <h3 class="step__title">Single<br>Tasking</h3>
    <p class="step__rate">$20 an Hour<br>Study Effort</p>
    <p class="step__text">The study environment is free of distractions (quiet, no phone, no TV, no social media, no email, no music with lyrics) with good organisation (eg effective homework diary use)</p>
  </section>

  <section class="step step--mindset">
    <svg class="step__icon" viewBox="0 0 36 36" fill="none" stroke="#fff" stroke-width="1.6" aria-hidden="true">
      <circle cx="18" cy="18" r="11"/><path d="M18 7 V29 M11 13 Q15 15 18 13 M25 13 Q21 15 18 13 M10 21 Q14 19 18 22 M26 21 Q22 19 18 22"/>
      <path d="M18 2 V5 M18 31 V34 M2 18 H5 M31 18 H34 M6 6 L8 8 M30 6 L28 8 M6 30 L8 28 M30 30 L28 28"/>
    </svg>
    <h3 class="step__title">The Right State<br>of Mind</h3>
    <p class="step__rate">$30 an Hour<br>Study Effort</p>
    <p class="step__text">Positive mindset toward the learning (self-directed), setting goals, enthusiastic about challenge) Planning of assignment efforts/revising between learning &amp; the exam - moving away from relying on the last minute and challenging procrastination Adequate sleep with good sleep habits</p>
  </section>

  <section class="step step--smarter">
    <svg class="step__icon" viewBox="0 0 36 36" fill="none" stroke="#fff" stroke-width="1.8" stroke-linejoin="round" aria-hidden="true">
      <circle cx="11" cy="8" r="5"/><path d="M11 5 V8 H13"/><rect x="18" y="12" width="14" height="10" rx="1"/><path d="M4 32 V22 Q4 17 10 17 H14 L18 24 H32 M2 32 H34 M24 24 V32"/>
    </svg>
    <h3 class="step__title">Studying<br>Smarter</h3>
    <p class="step__rate">$40 an Hour<br>Study Effort</p>
    <p class="step__text">Using effective study techniques - graphic organisers; practice questions; reflecting on study progress; hand writing notes short, sharp, distraction free periods of effort (pomodoro method), learning from feedback, spaced revision</p>
  </section>

  <section class="step step--balance">
    <svg class="step__icon" viewBox="0 0 36 36" fill="none" stroke="#fff" stroke-width="1.8" stroke-linejoin="round" aria-hidden="true">
      <path d="M4 12 Q4 6 9 6 Q11 6 12 8 Q13 6 15 6 Q20 6 20 12 Q20 16 12 20 Q4 16 4 12 Z"/><path d="M5 12 H9 L11 9 L13 14 L15 12 H19"/>
      <circle cx="28" cy="10" r="6"/><path d="M28 7 V10 H30"/><path d="M4 26 H32 M18 26 L14 33 H22 Z M18 20 V26"/>
    </svg>
    <h3 class="step__title">Balance<br>and Health</h3>
    <p class="step__rate">$50 an Hour<br>Study Effort</p>
    <p class="step__text">Study is supported by positive social, recreational &amp; health habits-Balance in life (exercise and healthy eating) &amp; community engagement</p>
  </section>

  <svg class="arrow-head" viewBox="0 0 180 38" aria-hidden="true">
    <polygon points="90,0 180,38 0,38" fill="var(--step6)"/>
  </svg>
  <section class="step step--aspire">
    <svg class="step__icon" viewBox="0 0 36 36" fill="none" stroke="#fff" stroke-width="1.8" stroke-linejoin="round" aria-hidden="true">
      <path d="M10 34 V26 Q4 22 5 14 Q7 3 19 3 Q31 4 31 15 L34 21 H31 V27 H25 V34"/>
      <circle cx="18" cy="15" r="4"/><path d="M18 8 V11 M18 19 V22 M11 15 H14 M22 15 H25 M13 10 L15 12 M23 10 L21 12 M13 20 L15 18 M23 20 L21 18"/>
    </svg>
    <h3 class="step__title">The<br>Aspirational<br>Step</h3>
    <p class="step__rate">$60 an Hour<br>Study Effort</p>
    <p class="step__text">• Flow -<br>'In the zone'- easy, productive study<br>• Purpose, intent, focus, stress control, positive mindset</p>
  </section>

  <div class="portrait portrait--one"><span role="img" aria-label="Portrait photograph of Walter Durning"></span></div>
  <blockquote class="quote quote--one">
    "We are what we repeatedly do.<br>Excellence, then, is not an act but a habit."
    <cite><span class="name">-Walter Durning,</span> <span class="role">American Writer and Philosopher</span></cite>
  </blockquote>

  <div class="portrait portrait--two"><span role="img" aria-label="Portrait photograph of Dean Jackson"></span></div>
  <blockquote class="quote quote--two">
    "Success in anything will always come down to this: Focus and Effort, and we control both of them."
    <cite><span class="name">-Dean "The Anchor" Jackson</span></cite>
    <small>(Photo by Carl Pinetti/Studio Press)</small>
  </blockquote>

  <div class="portrait portrait--three"><span role="img" aria-label="Portrait photograph of Pete Rowland"></span></div>
  <blockquote class="quote quote--three">
    "There are only two option regarding commitment. You are either in or you are out. There is no such thing as life in-between."
    <cite><span class="name">-Pete Rowland,</span> <span class="role">Pro Basketball Coach</span></cite>
    <small>(Photo by Wes Lorne/Studio Press)</small>
  </blockquote>

  <div class="footer-band"></div>
</main>
</body>
</html>
```